Global Expert Network Firm needs business card design

We need business card design for a new company based in Seoul, South Korea called 'Corwell Insight Partners'. We recruit industry experts covering all countries and connect our client and recruited expert by phone, face-to-face meetings and etc. We are a global expert network firm that is focused on delivering high-quality experts to our clients throughout the world. Our clients include multinational corporations, global consulting firms, private equity firms, venture capital firms, asset management companies.
We have made new logo and please find attachment.(Please use new logo)
Target Market(s)
Global Consulting Firms, Investment Firms, Private Equity Firms, Venture Capital Firms.
Industry/Entity Type
Recruitment
Contact Information for Business Card
We need two Languages (English and Korean Version).
The front is Korean and the back is English version.
[The back] [English]
Company Name: Corwell Insight Partners, Inc.
CEO Name: Derek Hwang
Address: #508, Daerim Bldg, 72 Mokdongseo-ro, Yangcheon-gu, Seoul, 07918, Korea
Tel. +82 2 847 1215
Fax. +82 2 761 4218
Mobile. +82 10 6284 1215
Email: derek@corwellip.com
Web: www.corwellip.com
[The front] [Korean] => Described in same order as English version.
회사명: 코웰인사이트파트너스(주)
대표이사: 황도윤
주소: 서울시 양천구 목동서로 72 대림빌딩 508호
Tel. 02 847 1215
Fax. 02 761 4218
Mobile. 010 6284 1215
Web: www.corwellip.com

```html
<!DOCTYPE html>
<html lang="en">
<head>
<meta charset="utf-8">
<title>Corwell Insight Partners – Business Cards</title>
<link rel="stylesheet" href="https://fonts.googleapis.com/css2?family=Roboto:wght@300;400&family=Noto+Sans+KR:wght@300;400&display=swap">
<style>
  :root {
    --bg: #f1f2f4;
    --navy: #1c2254;
    --navy-glow: #2a3270;
    --accent: #5aa9e6;
    --ink-light: #d9dcea;
    --ink-dark: #4a4d5a;
    --paper: #ffffff;
    --paper-shade: #eef0f4;
    --tagline-light: #8f95b8;
    --tagline-dark: #9a9dab;
  }
  * { box-sizing: border-box; margin: 0; padding: 0; }
  html, body { width: 1200px; height: 873px; overflow: hidden; }
  body {
    background: var(--bg);
    font-family: "Roboto", "Noto Sans KR", sans-serif;
    font-weight: 300;
  }
  .canvas {
    position: relative;
    width: 1200px;
    height: 873px;
    display: flex;
    align-items: center;
    justify-content: center;
    gap: 40px;
  }
  .card {
    position: relative;
    width: 540px;
    height: 300px;
    overflow: hidden;
    box-shadow: 0 2px 10px rgba(0,0,0,0.08);
  }
  .card--english { background: var(--navy); color: var(--ink-light); }
  .card--korean { background: var(--paper); color: var(--ink-dark); font-family: "Noto Sans KR", "Roboto", sans-serif; }

  .card__pattern {
    position: absolute; inset: 0;
    z-index: 0;
  }
  .card--english .card__pattern {
    background:
      radial-gradient(ellipse 60% 70% at 30% 80%, var(--navy-glow) 0%, transparent 70%),
      radial-gradient(ellipse 50% 60% at 75% 20%, var(--navy-glow) 0%, transparent 70%);
  }
  .card--korean .card__pattern {
    background:
      radial-gradient(ellipse 55% 65% at 70% 30%, var(--paper-shade) 0%, transparent 70%),
      radial-gradient(ellipse 45% 55% at 25% 85%, var(--paper-shade) 0%, transparent 70%);
  }
  .card > *:not(.card__pattern) { z-index: 1; }

  .card__person { position: absolute; left: 36px; top: 30px; }
  .card__name { color: var(--accent); font-size: 18px; font-weight: 400; letter-spacing: 0.2px; line-height: 22px; }
  .card--korean .card__name { font-size: 19px; font-weight: 300; letter-spacing: 2px; }
  .card__title { font-size: 12.5px; margin-top: 3px; line-height: 16px; }

  .contact-list { list-style: none; margin-top: 10px; }
  .contact-list li {
    display: flex; align-items: center; gap: 9px;
    font-size: 12.5px; line-height: 18px;
  }
  .contact-list svg { width: 12px; height: 12px; fill: var(--accent); flex: none; }

  .card__address {
    position: absolute; left: 36px; bottom: 28px;
    font-size: 12.5px; line-height: 18px;
  }

  .brand {
    position: absolute; right: 44px; bottom: 62px;
    text-align: left;
  }
  .brand__name {
    font-family: "Roboto", sans-serif;
    font-weight: 300;
    font-size: 21px;
    line-height: 27px;
    letter-spacing: 1.5px;
    text-transform: uppercase;
  }
  .card--english .brand__name { color: #ffffff; }
  .card--korean .brand__name { color: var(--navy); }
  .brand__tagline {
    margin-top: 8px;
    font-size: 6.5px;
    letter-spacing: 1.2px;
    text-transform: uppercase;
  }
  .card--english .brand__tagline { color: var(--tagline-light); }
  .card--korean .brand__tagline { color: var(--tagline-dark); }

  .card__accent-bar {
    position: absolute; right: 28px; bottom: 0;
    width: 116px; height: 5px;
    background: var(--accent);
  }
</style>
</head>
<body>
<main class="canvas">

  <svg width="0" height="0" style="position:absolute" aria-hidden="true">
    <defs>
      <symbol id="icon-phone" viewBox="0 0 12 12"><path d="M2.5 0.8 4.3 2.6 3.4 4.1C4.1 5.6 5.6 7.2 7.9 8.6L9.4 7.7 11.2 9.5 10 11.2C5.6 10.8 1.2 6.4 0.8 2Z"/></symbol>
      <symbol id="icon-fax" viewBox="0 0 12 12"><rect x="3" y="0.8" width="6" height="3.2"/><rect x="0.8" y="4.5" width="10.4" height="4.5" rx="1"/><rect x="3" y="8" width="6" height="3.2"/></symbol>
      <symbol id="icon-mobile" viewBox="0 0 12 12"><path d="M3.2 0.5h5.6a.8.8 0 0 1 .8.8v9.4a.8.8 0 0 1-.8.8H3.2a.8.8 0 0 1-.8-.8V1.3a.8.8 0 0 1 .8-.8Zm.6 1.4v7.4h4.4V1.9Z"/></symbol>
      <symbol id="icon-mail" viewBox="0 0 12 12"><path d="M0.8 2.3h10.4v7.4H0.8Z"/><path d="M1.8 3.2 6 6.5 10.2 3.2" fill="none" stroke="#ffffff" stroke-opacity="0.6" stroke-width="0.9"/></symbol>
      <symbol id="icon-web" viewBox="0 0 12 12"><circle cx="6" cy="6" r="5.2"/><path d="M0.8 6h10.4M6 0.8v10.4M2 3.5h8M2 8.5h8" stroke="#ffffff" stroke-opacity="0.6" stroke-width="0.7" fill="none"/></symbol>
    </defs>
  </svg>

  <section class="card card--english" aria-label="English side of business card">
    <div class="card__pattern" role="img" aria-label="Faint network of connected lines and nodes across the navy card"></div>
    <div class="card__person">
      <p class="card__name">Derek Hwang</p>
      <p class="card__title">CEO</p>
      <ul class="contact-list">
        <li><svg><use href="#icon-phone"/></svg>+82 2 847 1215</li>
        <li><svg><use href="#icon-fax"/></svg>+82 2 761 4218</li>
        <li><svg><use href="#icon-mobile"/></svg>+82 10 6284 1215</li>
        <li><svg><use href="#icon-mail"/></svg>derek@corwellip.com</li>
        <li><svg><use href="#icon-web"/></svg>www.corwellip.com</li>
      </ul>
    </div>
    <p class="card__address">#508, Daerim Bldg, 72 Mokdongseo-ro,<br>Yangcheon-gu, Seoul, 07918, Korea</p>
    <div class="brand">
      <p class="brand__name">Corwell<br>Insight<br>Partners</p>
      <p class="brand__tagline">Expert insight, worldwide</p>
    </div>
    <div class="card__accent-bar"></div>
  </section>

  <section class="card card--korean" lang="ko" aria-label="Korean side of business card">
    <div class="card__pattern" role="img" aria-label="Faint grey network of connected lines and nodes across the white card"></div>
    <div class="card__person">
      <p class="card__name">황도윤</p>
      <p class="card__title">대표이사</p>
      <ul class="contact-list">
        <li><svg><use href="#icon-phone"/></svg>02 847 1215</li>
        <li><svg><use href="#icon-fax"/></svg>02 761 4218</li>
        <li><svg><use href="#icon-mobile"/></svg>010 6284 1215</li>
        <li><svg><use href="#icon-mail"/></svg>derek@corwellip.com</li>
        <li><svg><use href="#icon-web"/></svg>www.corwellip.com</li>
      </ul>
    </div>
    <p class="card__address">서울시 양천구 목동서로 72 대림빌딩 508호</p>
    <div class="brand">
      <p class="brand__name">Corwell<br>Insight<br>Partners</p>
      <p class="brand__tagline">Expert insight, worldwide</p>
    </div>
    <div class="card__accent-bar"></div>
  </section>

</main>
</body>
</html>
```